Lumo Pharma Chinese Traditional Medicine Web Design

We need a web design for a new company based in Shanghai China called 'Lumo Pharma'. We develop Chinese traditional herbal medicine, including research and development, technical support service, manufacturing, . Also, there’s a small ratio of western medicine. Our goal is to contributing to a healthier future.

Target Market(s)

global,but mainly China

Industry/Entity Type

Pharmaceutical

Number of Pages Required

1 page

Font styles to use
Serif

Colors
e4daeb
cedeed
cadf82
eaf2ce
fbd4d5
fee3d4
fabb94
fee18a
b8a6cd

Requirements
Must have
• triditional Chinese elements, concept of herbal, health, value, better life for people..could be colourful but not more than 3 different colour..
Nice to have
• Style: simple, communicate traditional Chinese herbal medicine element, as well as modern technique..same as LOGO style..
Should not have
• please dont show more IT elements...

```html
<!DOCTYPE html>
<html lang="zh">
<head>
<meta charset="utf-8">
<title>Lumo Pharma</title>
<link href="https://fonts.googleapis.com/css2?family=Noto+Serif+SC:wght@400;500;700&family=Nunito+Sans:wght@400;600;700&display=swap" rel="stylesheet">
<style>
:root{
  --lavender:#b8a6cd;
  --lavender-soft:#e4daeb;
  --leaf:#cadf82;
  --leaf-soft:#eaf2ce;
  --peach:#fabb94;
  --ink:#4a4a4a;
  --ink-soft:#5c5c5c;
  --mist:#f6f6f8;
  --night:#3b3544;
  --white:#ffffff;
}
*{margin:0;padding:0;box-sizing:border-box}
html,body{width:1200px;height:2287px;overflow:hidden;background:var(--white)}
body{position:relative;font-family:"Nunito Sans",Arial,sans-serif;color:var(--ink)}
.serif{font-family:"Noto Serif SC",serif}
.abs{position:absolute}
.topbar{left:0;top:0;width:1200px;height:25px;background:var(--lavender);color:var(--white);font:10px "Noto Serif SC",serif;line-height:25px}
.topbar .addr{left:173px}
.topbar .lic{right:175px}
.header{left:0;top:25px;width:1200px;height:57px;background:var(--white)}
.brand{left:173px;top:16px;display:flex;align-items:center;gap:6px;font:600 12px "Noto Serif SC",serif;color:#7a5a3c}
.brand i{width:12px;height:12px;border-radius:50%;background:var(--leaf);display:block}
.nav{left:607px;top:19px;display:flex;gap:28px;font:11px "Noto Serif SC",serif;color:#333}
.hero{left:0;top:82px;width:1200px;height:560px;overflow:hidden}
.hero-photo{position:absolute;inset:0;background:linear-gradient(100deg,#9fb8b0 0%,#7fa7c4 45%,#e8eef2 75%,#f2f4f6 100%)}
.hero svg{position:absolute;left:0;top:0}
.hero h1{position:absolute;left:173px;color:var(--white);font-weight:500}
.hero .h-cn{top:95px;font:500 63px/1 "Noto Serif SC",serif}
.hero .h-en{top:178px;font:700 62px/1 "Nunito Sans",sans-serif;letter-spacing:1px}
.hero p{position:absolute;left:173px;top:256px;color:var(--white);font:15px/21px "Noto Serif SC",serif;width:440px}
.btn{position:absolute;width:131px;height:36px;background:var(--peach);color:var(--white);font:500 16px/36px "Noto Serif SC",serif;text-align:center;letter-spacing:2px}
.hero .btn{left:173px;top:357px;width:138px;height:37px;line-height:37px}
.counter{left:173px;top:480px;color:var(--white);font:700 27px "Nunito Sans",sans-serif}
.counter span{color:rgba(255,255,255,.5)}
.sec-title{font:500 52px/1 "Noto Serif SC",serif;color:var(--ink-soft);letter-spacing:4px}
.bar{width:46px;height:4px;background:var(--lavender)}
.body-text{font:11.5px/15px "Nunito Sans",sans-serif;color:var(--ink-soft)}
.about-title{left:173px;top:730px}
.about-bar{left:173px;top:786px}
.about-text{left:173px;top:805px;width:330px}
.ticks{left:173px;top:922px;list-style:none;font-size:10.5px;color:#333}
.ticks li{height:21px;padding-left:12px;position:relative}
.ticks li::before{content:"";position:absolute;left:0;top:5px;width:5px;height:5px;background:var(--leaf)}
.about-btn{left:174px;top:1022px}
.photo-lab{left:571px;top:761px;width:454px;height:292px;background:linear-gradient(120deg,#dfe8ee 0%,#eef3f6 45%,#cfd9df 100%)}
.photo-herb{left:533px;top:730px;width:215px;height:292px;background:radial-gradient(circle at 40% 45%,#6b5a9a 0%,#2b2440 55%,#0f0f14 100%)}
.divider{left:173px;top:1131px;width:852px;height:1px;background:#e2e2e2}
.feature{width:220px;text-align:center;top:1165px}
.feature svg{display:block;margin:0 auto}
.feature h3{margin-top:22px;font:500 25px "Noto Serif SC",serif;color:var(--ink-soft);letter-spacing:2px}
.feature p{margin-top:10px;font:11.5px/15px "Nunito Sans",sans-serif;color:var(--ink-soft)}
.arrow{top:1220px}
.products{left:0;top:1423px;width:1200px;height:474px;background:var(--mist)}
.photo-scientist{left:0;top:1423px;width:690px;height:474px;background:linear-gradient(90deg,#8fc6e0 0%,#cfe6f2 40%,#eef2f6 80%,rgba(246,246,248,0) 100%)}
.prod-title{left:645px;top:1535px;font-size:55px}
.prod-bar{left:645px;top:1597px}
.prod-text{left:645px;top:1615px;width:340px}
.services{left:645px;top:1696px;display:flex;gap:20px;font:500 16px "Noto Serif SC",serif;color:#444}
.services div{display:flex;align-items:center;gap:7px}
.prod-btn{left:648px;top:1751px}
.partners{left:173px;top:1944px;width:852px;height:54px}
.partner{top:14px;height:26px;background:#c9c9cc;border-radius:3px}
.footer{left:0;top:2046px;width:1200px;height:241px;background:linear-gradient(90deg,#3f3849 0%,#362f3e 50%,#403945 100%);color:var(--white)}
.foot-brand{left:200px;top:79px;font:500 14px "Noto Serif SC",serif;display:flex;align-items:center;gap:8px}
.foot-brand i{width:16px;height:16px;border-radius:50%;background:var(--lavender);display:block}
.foot-brand small{display:block;font-size:10px;color:#ddd;text-align:center}
.fcol h4{font:700 13.5px "Nunito Sans",sans-serif;margin-bottom:12px}
.fcol{font-size:10px;line-height:21px}
.quick{left:350px;top:52px}
.quick a{display:block;color:var(--white);text-decoration:none;font:600 10px/21px "Noto Serif SC",serif}
.blog{left:509px;top:52px;line-height:14px}
.blog .d{font-weight:700;font-size:9px;margin-bottom:14px}
.contact{left:862px;top:52px;line-height:16px}
.follow{left:863px;top:126px}
.socials{display:flex;gap:4px;margin-top:2px}
.socials span{width:17px;height:17px;border-radius:50%;background:#9b8fae;display:block}
.foot-line{left:0;top:186px;width:1200px;height:1px;background:rgba(255,255,255,.25)}
.copy{left:0;top:207px;width:1200px;text-align:center;font-size:10.5px}
</style>
</head>
<body>

<div class="abs topbar">
  <span class="abs addr">中国（上海）自由贸易试验区明德路88号）</span>
  <span class="abs lic">京公网安备 12010000000000号</span>
</div>

<header class="abs header">
  <div class="abs brand"><i></i>LUMO PHARMA</div>
  <nav class="abs nav"><span>公司首页</span><span>公司概况</span><span>新闻中心</span><span>产品服务</span><span>职业发展</span><span>联系我们</span></nav>
</header>

<section class="abs hero">
  <div class="hero-photo" role="img" aria-label="Gloved hands holding amber medicine vials in a laboratory"></div>
  <svg width="1200" height="560" aria-hidden="true"><polygon points="0,0 788,0 532,560 0,560" fill="#cadf82" fill-opacity=".55"/></svg>
  <h1 class="h-cn">欢迎来到</h1>
  <h1 class="h-en">LUMO PHARMA</h1>
  <p>LUMO Pharma是一家制药公司，于2019年在中国上海注册，致力于研发中草药，包括研发，技术支持服务，制造以及顶级专家团队。而且，西医的比例很小。</p>
  <div class="btn">学到更多</div>
  <div class="abs counter">21/ <span>1</span></div>
</section>

<h2 class="abs sec-title about-title">公司简介</h2>
<div class="abs bar about-bar"></div>
<p class="abs body-text about-text">Lorem ipsum dolor sit amet, consectetur adipiscing elit, sed do eiusmod tempor incididunt ut labore et dolore magna aliqua. Ut enim ad minim veniam, quis nostrud exercitation ullamco laboris nisi ut aliquip ex ea commodo consequat. Duis aute irure dolor in reprehenderit in voluptate velit esse cillum dolore eu fugiat nulla pariatur. Excepteur sint occaecat cupidatat non proident, sunt in culpa qui officia deserunt mollit anim id est laborum.</p>
<ul class="abs ticks">
  <li>Ut enim ad minim veniam, quis nostrud exercitation ullamco</li>
  <li>Duis aute irure dolor in reprehenderit in voluptate</li>
  <li>Excepteur sint occaecat cupidatat non proident, sunt in culpa</li>
  <li>Lorem ipsum dolor sit amet, consectetur adipiscing</li>
</ul>
<div class="btn about-btn">学到更多</div>
<div class="abs photo-lab" role="img" aria-label="Researcher in mask and goggles looking into a microscope"></div>
<div class="abs photo-herb" role="img" aria-label="Purple herbal flowers beside jars of cream and white pills"></div>

<div class="abs divider"></div>

<div class="abs feature" style="left:170px">
  <svg width="72" height="72" viewBox="0 0 72 72" fill="none" stroke="#b8a6cd" stroke-width="3"><circle cx="36" cy="28" r="10"/><circle cx="36" cy="28" r="4"/><path d="M36 38v28M36 52h7M36 60h6"/><path d="M18 30a18 18 0 0 1 36 0"/><circle cx="12" cy="38" r="4"/><circle cx="60" cy="38" r="4"/><circle cx="22" cy="14" r="3"/><circle cx="50" cy="14" r="3"/><circle cx="36" cy="5" r="3"/></svg>
  <h3>关键能力</h3>
  <p>Duis aute irure dolor in reprehenderit in voluptate velit esse cillum dolore eu fugiat nulla pariatur.</p>
</div>
<div class="abs feature" style="left:490px">
  <svg width="72" height="72" viewBox="0 0 72 72" fill="none" stroke="#b8a6cd" stroke-width="3"><circle cx="36" cy="36" r="28"/><circle cx="36" cy="36" r="16"/><circle cx="36" cy="32" r="5"/><path d="M28 45a8 8 0 0 1 16 0"/><circle cx="36" cy="6" r="4"/><circle cx="36" cy="66" r="4"/><circle cx="6" cy="36" r="4"/><circle cx="66" cy="36" r="4"/></svg>
  <h3>合作伙伴</h3>
  <p>Duis aute irure dolor in reprehenderit in voluptate velit esse cillum dolore eu fugiat nulla pariatur.</p>
</div>
<div class="abs feature" style="left:808px">
  <svg width="72" height="72" viewBox="0 0 72 72" fill="none" stroke="#b8a6cd" stroke-width="3"><path d="M36 8c8 8 10 20 0 40c-10-20-8-32 0-40z"/><path d="M36 48c-4-14-14-24-22-26c0 14 8 24 22 26z"/><path d="M36 48c4-14 14-24 22-26c0 14-8 24-22 26z"/><path d="M36 56c-12 0-24-6-30-18c10-2 20 2 30 18c10-16 20-20 30-18c-6 12-18 18-30 18z"/></svg>
  <h3>企业文化</h3>
  <p>Duis aute irure dolor in reprehenderit in voluptate velit esse cillum dolore eu fugiat nulla pariatur.</p>
</div>
<svg class="abs arrow" style="left:428px" width="22" height="14" viewBox="0 0 22 14" fill="none" stroke="#bbb" stroke-width="2"><path d="M1 7h19M14 1l6 6-6 6"/></svg>
<svg class="abs arrow" style="left:751px" width="22" height="14" viewBox="0 0 22 14" fill="none" stroke="#bbb" stroke-width="2"><path d="M1 7h19M14 1l6 6-6 6"/></svg>

<section class="abs products"></section>
<div class="abs photo-scientist" role="img" aria-label="Scientist in cap and goggles using a pipette over blue test tubes"></div>
<h2 class="abs sec-title prod-title">产品服务</h2>
<div class="abs bar prod-bar"></div>
<p class="abs body-text prod-text">Lorem ipsum dolor sit amet, consectetur adipiscing elit, sed do eiusmod tempor incididunt ut labore et dolore magna aliqua. Ut enim ad minim veniam, quis nostrud exercitation ullamco laboris nisi ut aliquip ex ea commodo consequat.</p>
<div class="abs services">
  <div><svg width="24" height="28" viewBox="0 0 24 28" fill="none" stroke="#b8a6cd" stroke-width="2"><circle cx="12" cy="11" r="9"/><circle cx="12" cy="11" r="4"/><path d="M8 20l-2 7 6-3 6 3-2-7"/></svg>中药研发</div>
  <div><svg width="30" height="28" viewBox="0 0 30 28" fill="none" stroke="#b8a6cd" stroke-width="2"><circle cx="15" cy="7" r="4"/><path d="M8 18a7 7 0 0 1 14 0"/><path d="M2 12l5 10h16l5-10"/><path d="M7 22v5M23 22v5"/></svg>技术咨询服务</div>
</div>
<div class="btn prod-btn">学到更多</div>

<div class="abs partners">
  <div class="abs partner" style="left:4px;width:126px"></div>
  <div class="abs partner" style="left:196px;width:106px"></div>
  <div class="abs partner" style="left:362px;width:142px"></div>
  <div class="abs partner" style="left:569px;width:108px"></div>
  <div class="abs partner" style="left:748px;width:94px"></div>
</div>

<footer class="abs footer">
  <div class="abs foot-brand"><i></i><div>LUMO PHARMA<small>陆茂医药</small></div></div>
  <div class="abs fcol quick"><h4>Quick Links</h4><a>公司首页</a><a>公司概况</a><a>新闻中心</a><a>产品服务</a></div>
  <div class="abs fcol blog"><h4>Latest From Blog</h4>
    <div>HerbLink Now Runs Cloud-Based POS</div><div class="d">April 6, 2015</div>
    <div>Jade Garden Adds Brightwave Smart TV as Ordering Platform</div><div class="d">April 1, 2015</div>
  </div>
  <div class="abs fcol contact"><h4>Contact</h4><div>Email: info@lumopharma.com</div><div>Phone: (123) 555-0142</div></div>
  <div class="abs fcol follow"><h4 style="margin-bottom:6px">Follow Us</h4><div class="socials"><span></span><span></span><span></span></div></div>
  <div class="abs foot-line"></div>
  <div class="abs copy">© 2020 Lumo Pharma Chinese Traditional Medicine, All Rights Reserved</div>
</footer>

</body>
</html>
```